Cutting Edge Cloud Hosting Provider needs business card design

We are a new Cloud Hosting Provider called Velkaro Hosting. (Velkaro means cloudy in Spanish.) We provide clients with virtual resources and not virtual machines directly. Our clients purchase the resources that they will use (RAM,CPU, Hard drive space) then use those resources in as many virtual machines as they like.

We are looking for a business card design that is cutting edge and hip.
Updates

The name of the company is "Velkaro Hosting". Please include the "Hosting" part of our name in the design.

Thanks

Target Market(s)

21-35 developers and I.T. Staff

Industry/Entity Type

Business

Requirements
Must have
• Rounded corners, Must Incorporate our logo, individual's name must be prominent

```html
<!DOCTYPE html>
<html lang="en">
<head>
<meta charset="utf-8">
<title>Velkaro Hosting – Business Card</title>
<link rel="stylesheet" href="https://fonts.googleapis.com/css2?family=Noto+Sans:wght@400;600&display=swap">
<style>
  :root {
    --page-bg: #f1f1f1;
    --card-bg: #f0f0f0;
    --band-green: #9aae22;
    --band-blue: #a9cbe4;
    --name-green: #93ad1f;
    --ink-blue: #2a3e9a;
    --brand-navy: #1b2a6b;
  }
  * { margin: 0; padding: 0; box-sizing: border-box; }
  html, body { width: 1200px; height: 900px; overflow: hidden; }
  body {
    background: radial-gradient(ellipse at 50% 45%, #ffffff 0%, var(--page-bg) 75%);
    font-family: "Noto Sans", Verdana, sans-serif;
    position: relative;
  }
  .card {
    position: absolute;
    top: 304px;
    width: 540px;
    height: 300px;
    border-radius: 18px;
    overflow: hidden;
    background: var(--card-bg);
    box-shadow: 0 3px 8px rgba(0,0,0,0.35);
  }
  .card--front { left: 42px; }
  .card--back { left: 627px; }
  .card__band {
    position: absolute; left: 0; top: 0;
    width: 540px; height: 84px;
    background: linear-gradient(180deg, var(--band-green) 0%, var(--band-green) 55%, var(--band-blue) 85%, var(--card-bg) 100%);
  }
  .person-name {
    position: absolute; left: 28px; top: 118px;
    font-size: 36px; font-weight: 400; color: var(--name-green); line-height: 1;
  }
  .person-title {
    position: absolute; left: 62px; top: 160px;
    font-size: 15px; font-weight: 400; color: var(--ink-blue); line-height: 1;
  }
  .brand-name {
    position: absolute; top: 168px;
    font-size: 30px; font-weight: 600; color: var(--brand-navy); line-height: 1;
    white-space: nowrap;
  }
  .card--front .brand-name { right: 26px; }
  .card--back .brand-name { left: 0; right: 0; text-align: center; top: 158px; font-size: 34px; }
  .contact {
    position: absolute; left: 36px; top: 222px;
    font-size: 15px; line-height: 19px; color: var(--ink-blue);
    list-style: none;
  }
  .contact__email { color: var(--name-green); padding-left: 8px; }
</style>
</head>
<body>
  <section class="card card--front">
    <div class="card__band" role="img" aria-label="Decorative cloud border in green and light blue"></div>
    <h1 class="person-name">Tomas Alder</h1>
    <p class="person-title">Vice-President</p>
    <p class="brand-name">Velkaro Hosting</p>
    <ul class="contact">
      <li class="contact__email">tomas@velkaro.com</li>
      <li>call:- p. 210.555.0142</li>
      <li>call:- c. 210.555.0187</li>
    </ul>
  </section>

  <section class="card card--back">
    <div class="card__band" role="img" aria-label="Decorative cloud border in green and light blue"></div>
    <p class="brand-name">Velkaro Hosting</p>
  </section>
</body>
</html>
```